Aviation Banner Ad Designs

SkyLedgerMetrics provides access to the most accurate aircraft operating cost information, to compare Piston, Turboprop and Jet aircraft.

The banners ads will be used for retargeting/remarketing - to bring visitors back to the site. The banners should remind and reinforce the key messages of what the site provides.

Target Market(s)

Private aircraft buyers including:
- Aircraft Brokers
- Charter Operators
- Corporate Flight Departments
- Aircraft Management companies
- Financial Institutions
- Aircraft Owners
- Prospective Buyers

Requirements
Must have
• A. Banner Objective
The visual and textual content of the banner should remind the viewer about the features of the site, and prompt them to return to the site.
1. Arresting visual
2. Headline
3. Single message
4. Compelling CTA
5. Logo - big enough to see
6. Standard DWR ad sizes/specs

B. Design Elements
Logo: As attached
Main Title: Calculate Jet Operating Costs
Subtitle: Compare Ownership Usage Scenarios
Call to Action Button: Compare Ownership Costs
Background: Several images supplied as options

C. Banner Sizes
Do examples as 300×250 , 728×90 , 160×600
Final sizes to also include 320×100 , 336x280 , 300x600

Finally delivery as .jpg files.

Font - use same font as on site

```html
<!DOCTYPE html>
<html lang="en">
<head>
<meta charset="utf-8">
<title>SkyLedgerMetrics – Calculate Jet Operating Costs</title>
<link rel="stylesheet" href="https://fonts.googleapis.com/css2?family=Roboto+Condensed:ital,wght@0,700;1,700&display=swap">
<style>
  :root {
    --white: #ffffff;
    --ink: #141414;
    --headline-green: #1ea33a;
    --sub-red: #e1251b;
    --sky-light: #e6eef5;
    --sky-mid: #b9cbda;
    --steel: #8c9fb1;
    --brand-accent: #2a63b4;
  }
  html, body {
    margin: 0;
    padding: 0;
    width: 1200px;
    height: 148px;
    overflow: hidden;
    background: var(--white);
  }
  .banner {
    position: relative;
    width: 1200px;
    height: 148px;
    overflow: hidden;
    background: var(--white);
    font-family: "Roboto Condensed", "Arial Narrow", sans-serif;
  }
  .banner__backdrop {
    position: absolute;
    left: 0;
    top: 0;
    width: 620px;
    height: 148px;
    background:
      linear-gradient(90deg, rgba(255,255,255,0) 55%, var(--white) 100%),
      radial-gradient(ellipse at 30% 60%, var(--sky-mid) 0%, var(--sky-light) 55%, var(--white) 100%);
  }
  .banner__headline {
    position: absolute;
    left: 16px;
    top: 30px;
    margin: 0;
    font-size: 31px;
    line-height: 1;
    font-style: italic;
    font-weight: 700;
    text-transform: uppercase;
    color: var(--headline-green);
    letter-spacing: 0.2px;
    background: rgba(255,255,255,0.85);
    padding: 2px 6px;
  }
  .banner__subline {
    position: absolute;
    left: 34px;
    top: 80px;
    margin: 0;
    font-size: 25px;
    line-height: 1;
    font-style: italic;
    font-weight: 700;
    color: var(--sub-red);
    background: rgba(255,255,255,0.85);
    padding: 2px 6px;
  }
  .banner__devices {
    position: absolute;
    left: 535px;
    top: 12px;
    width: 330px;
    height: 128px;
    border-radius: 6px;
    background: linear-gradient(180deg, #f3f5f8 0%, #d9dee5 100%);
  }
  .brand {
    position: absolute;
    left: 905px;
    top: 24px;
    display: flex;
    align-items: center;
    gap: 10px;
  }
  .brand__mark {
    width: 30px;
    height: 30px;
    background: var(--brand-accent);
  }
  .brand__name {
    font-size: 34px;
    font-weight: 700;
    color: var(--ink);
    line-height: 1;
  }
  .cta {
    position: absolute;
    left: 874px;
    top: 92px;
    width: 294px;
    height: 40px;
    box-sizing: border-box;
    border: 2px solid var(--ink);
    background: var(--white);
    display: flex;
    align-items: center;
    justify-content: center;
    font-size: 20px;
    font-weight: 700;
    text-transform: uppercase;
    color: var(--ink);
    text-decoration: none;
    letter-spacing: 0.3px;
  }
</style>
</head>
<body>
  <div class="banner">
    <div class="banner__backdrop" role="img" aria-label="Close-up of a business jet engine nacelle against a pale sky"></div>
    <h1 class="banner__headline">Calculate Jet Operating Costs</h1>
    <p class="banner__subline">Compare Ownership Usage Scenarios</p>
    <div class="banner__devices" role="img" aria-label="Phone, tablet, monitor and laptop showing aircraft cost charts and jet diagrams"></div>
    <div class="brand">
      <span class="brand__mark"></span>
      <span class="brand__name">SkyLedgerMetrics</span>
    </div>
    <a class="cta" href="#">Compare Ownership Costs</a>
  </div>
</body>
</html>
```